Need UI design for an iOS app game with most of the layout planned

The name of the game is "QUADRIX".

The goal of the game is to find a way to manipulate four numbers so that the end result is 24. Addition, subtraction, multiplication and division may be used and each number can only be used once.

The list of items we need is:

1. launch image, app icon, UI design of all scenes (10-12 scenes) of the app.
2. App background image should support screen size of both 640x1136.
3. Files are preferred to be in (.eps) format so that resolution can be adjusted later. But other file formats are welcome as long as resolution is high enough.
4. Icons, buttons, background image etc. should have their own file so that later they can be moved around in case design is changed.

The detailed requirement is in the attached file. The actual layout can vary if it can help achieve better result. We also attached several screenshots from iOS game "Glimtor". You can use that as your reference.

```html
<!DOCTYPE html>
<html lang="en">
<head>
<meta charset="utf-8">
<title>QUADRIX – Home</title>
<link rel="stylesheet" href="https://fonts.googleapis.com/css2?family=Arimo:wght@400;700&display=swap">
<style>
  :root {
    --status-bg: #000000;
    --status-text: #ffffff;
    --sky-top: #3d9edc;
    --sky-mid: #3592d5;
    --sky-bottom: #2a84c9;
    --swirl: rgba(255, 255, 255, 0.18);
    --header-line: rgba(20, 90, 150, 0.45);
    --header-glow: rgba(255, 255, 255, 0.12);
    --white: #ffffff;
    --btn-primary-text: #4a98d4;
    --btn-primary-border: #cfe2f1;
    --btn-secondary-bg: #1f70ac;
    --btn-secondary-border: #15568a;
    --cloud-a: rgba(40, 110, 170, 0.55);
    --cloud-b: rgba(120, 180, 225, 0.35);
  }
  * { box-sizing: border-box; margin: 0; padding: 0; }
  html, body { width: 676px; height: 1200px; overflow: hidden; }
  body { font-family: "Arimo", Arial, sans-serif; background: var(--sky-mid); }

  .screen {
    position: relative;
    width: 676px;
    height: 1200px;
    overflow: hidden;
    background: linear-gradient(180deg, var(--sky-top) 0%, var(--sky-mid) 55%, var(--sky-bottom) 100%);
  }
  .backdrop-swirls { position: absolute; inset: 0; }

  .status-bar {
    position: absolute; top: 0; left: 0; right: 0; height: 42px;
    background: var(--status-bg); color: var(--status-text);
    display: flex; align-items: center; justify-content: space-between;
    padding: 0 10px; font-size: 26px;
  }
  .status-left { display: flex; align-items: center; gap: 8px; }
  .status-time { position: absolute; left: 0; right: 0; text-align: center; pointer-events: none; }
  .status-right { display: flex; align-items: center; gap: 12px; }

  .app-header {
    position: absolute; top: 42px; left: 0; right: 0; height: 96px;
    background: linear-gradient(180deg, var(--header-glow), transparent);
    border-bottom: 2px solid var(--header-line);
  }
  .header-title {
    position: absolute; left: 0; right: 0; top: 30px;
    text-align: center; color: var(--white);
    font-size: 27px; font-weight: 700; letter-spacing: 2px;
  }
  .header-icon { position: absolute; top: 25px; width: 44px; height: 44px; }
  .header-icon.settings { left: 28px; }
  .header-icon.info { right: 28px; }

  .hero-art {
    position: absolute; left: 69px; top: 248px; width: 544px; height: 386px;
    border-radius: 48% 52% 45% 55% / 50% 48% 52% 50%;
    background:
      radial-gradient(ellipse at 45% 40%, var(--cloud-a), transparent 70%),
      radial-gradient(ellipse at 70% 55%, var(--cloud-b), transparent 65%);
  }
  .game-title {
    position: absolute; left: 0; right: 0; top: 370px;
    text-align: center; color: var(--white);
    font-size: 104px; font-weight: 700; letter-spacing: 4px; line-height: 1;
  }

  .menu-button {
    position: absolute; left: 97px; width: 482px; height: 72px;
    border-radius: 13px;
    display: flex; align-items: center; justify-content: center;
    font-size: 33px; font-weight: 700;
  }
  .menu-button.single {
    top: 789px; background: var(--white); color: var(--btn-primary-text);
    border: 2px solid var(--btn-primary-border);
  }
  .menu-button.multi {
    top: 965px; background: var(--btn-secondary-bg); color: var(--white);
    border: 2px solid var(--btn-secondary-border);
  }
</style>
</head>
<body>
<main class="screen">
  <svg class="backdrop-swirls" width="676" height="1200" viewBox="0 0 676 1200" aria-hidden="true">
    <path d="M-20 300 C 150 180, 420 120, 700 170" fill="none" stroke="var(--swirl)" stroke-width="3"/>
    <path d="M-20 690 C 200 760, 480 760, 700 560" fill="none" stroke="var(--swirl)" stroke-width="3"/>
    <path d="M-20 1080 C 200 1040, 460 1100, 700 1010" fill="none" stroke="var(--swirl)" stroke-width="4"/>
    <path d="M-20 1160 C 240 1120, 460 1180, 700 1120" fill="none" stroke="var(--swirl)" stroke-width="2"/>
    <path d="M420 140 C 620 240, 690 420, 600 640" fill="none" stroke="var(--swirl)" stroke-width="2"/>
  </svg>

  <div class="status-bar">
    <div class="status-left">
      <svg width="42" height="16" viewBox="0 0 42 16" aria-hidden="true">
        <rect x="0" y="10" width="6" height="6" fill="#fff"/>
        <rect x="8" y="7" width="6" height="9" fill="#fff"/>
        <rect x="16" y="4" width="6" height="12" fill="#fff"/>
        <rect x="24" y="2" width="6" height="14" fill="#fff"/>
        <rect x="32" y="0" width="6" height="16" fill="#fff"/>
      </svg>
      <span class="carrier">Telvo</span>
    </div>
    <span class="status-time">4:20 PM</span>
    <div class="status-right">
      <svg width="22" height="22" viewBox="0 0 22 22" aria-hidden="true">
        <circle cx="11" cy="11" r="10" fill="#fff"/>
        <path d="M11 5 V11 H15" stroke="#000" stroke-width="2" fill="none"/>
      </svg>
      <svg width="22" height="22" viewBox="0 0 22 22" aria-hidden="true">
        <path d="M21 1 L1 9 L10 12 L13 21 Z" fill="#fff"/>
      </svg>
      <svg width="28" height="28" viewBox="0 0 28 28" aria-hidden="true">
        <path d="M24 14 A10 10 0 1 1 14 4" fill="none" stroke="#fff" stroke-width="2.5"/>
        <rect x="9" y="12" width="10" height="8" fill="#fff"/>
        <path d="M11 12 V9 A3 3 0 0 1 17 9 V12" fill="none" stroke="#fff" stroke-width="2"/>
      </svg>
      <svg width="44" height="20" viewBox="0 0 44 20" aria-hidden="true">
        <rect x="1" y="1" width="38" height="18" rx="3" fill="none" stroke="#fff" stroke-width="2"/>
        <rect x="4" y="4" width="32" height="12" fill="#fff"/>
        <rect x="40" y="6" width="3" height="8" fill="#fff"/>
      </svg>
    </div>
  </div>

  <header class="app-header">
    <svg class="header-icon settings" viewBox="0 0 44 44" aria-label="Settings" role="img">
      <circle cx="22" cy="22" r="20" fill="none" stroke="#fff" stroke-width="2.5"/>
      <circle cx="18" cy="25" r="6" fill="none" stroke="#fff" stroke-width="3.5" stroke-dasharray="3 2"/>
      <circle cx="18" cy="25" r="2" fill="#fff"/>
      <circle cx="28" cy="16" r="4" fill="none" stroke="#fff" stroke-width="3" stroke-dasharray="2.5 1.5"/>
    </svg>
    <h1 class="header-title">QUADRIX</h1>
    <svg class="header-icon info" viewBox="0 0 44 44" aria-label="About" role="img">
      <circle cx="22" cy="22" r="20" fill="none" stroke="#fff" stroke-width="2.5"/>
      <rect x="19.5" y="10" width="5" height="16" rx="2.5" fill="#fff"/>
      <circle cx="22" cy="32" r="3" fill="#fff"/>
    </svg>
  </header>

  <div class="hero-art" role="img" aria-label="Cloud of arithmetic symbols: plus, minus, multiply, divide and equals signs in speech bubbles"></div>
  <p class="game-title">QUADRIX</p>

  <a class="menu-button single" href="#single">Single Player</a>
  <a class="menu-button multi" href="#multi">Multi Player</a>
</main>
</body>
</html>
```